Verdel Harvest Co - Business Card Design Project

We need business cards for our business. We grow roots and fruits in Central and South America, we import and distribute in FL, USA. We do fresh and frozen products.

Target Market(s)

Small and big supermarkets, wholesalers, traders, distributors, etc

Industry/Entity Type

Business

```html
<!DOCTYPE html>
<html lang="en">
<head>
<meta charset="UTF-8">
<title>Verdel Harvest Co – Business Card</title>
<link href="https://fonts.googleapis.com/css2?family=Montserrat:wght@500;600;700&display=swap" rel="stylesheet">
<style>
  :root {
    --page-bg: #e4e4e2;
    --card-bg: #ffffff;
    --brand-green: #526a33;
    --rule-green: #5a6b2c;
    --text-grey: #5a5a5a;
  }
  * { margin: 0; padding: 0; box-sizing: border-box; }
  html, body {
    width: 1200px;
    height: 898px;
    overflow: hidden;
    background: var(--page-bg);
    font-family: "Montserrat", Arial, sans-serif;
  }
  .card {
    position: absolute;
    left: 180px;
    top: 209px;
    width: 840px;
    height: 480px;
    background: var(--card-bg);
    box-shadow: 0 10px 30px rgba(0,0,0,0.15);
  }
  .side-band {
    position: absolute;
    left: 0;
    top: 0;
    width: 92px;
    height: 100%;
    background: var(--brand-green);
  }
  .brand-name {
    position: absolute;
    left: 132px;
    top: 62px;
    font-size: 30px;
    font-weight: 600;
    color: var(--brand-green);
    letter-spacing: 0.5px;
  }
  .person-name {
    position: absolute;
    right: 40px;
    top: 118px;
    font-size: 30px;
    font-weight: 700;
    color: var(--brand-green);
    letter-spacing: 0.5px;
  }
  .rule {
    position: absolute;
    height: 2px;
    background: var(--rule-green);
  }
  .rule--name { left: 470px; right: 0; top: 166px; }
  .rule--contact { left: 132px; width: 420px; top: 318px; }
  .contact {
    position: absolute;
    left: 132px;
    top: 340px;
    color: var(--text-grey);
    list-style: none;
  }
  .contact__phone { font-size: 26px; font-weight: 500; margin-bottom: 10px; }
  .contact__line { font-size: 20px; font-weight: 500; margin-bottom: 8px; }
</style>
</head>
<body>
  <div class="card">
    <div class="side-band"></div>
    <div class="brand-name">Verdel Harvest Co</div>
    <div class="person-name">MATEO RUIZ</div>
    <div class="rule rule--name"></div>
    <div class="rule rule--contact"></div>
    <ul class="contact">
      <li class="contact__phone">0455501872</li>
      <li class="contact__line">support@verdelharvest.com</li>
      <li class="contact__line">www.verdelharvest.com</li>
    </ul>
  </div>
</body>
</html>
```